Kalvoria - a property developer - Website design

Hi all!
Exciting new project for you! :)
We are looking for some creative/modern designs to best represent us as a company.
Please have a look at the following link: huhu.kalvoria.example to get an idea about who we are and what we do.
The 'Main Page' of the HP should be neatly arranged, easy to navigate, contain several pictures (changing every 10 seconds or so) that should reflect that we are property developers.
The navigation points ('About us', 'Projects' 'Investment', 'Contact Us', 'Legal Notice') should be included in the Design (again under every navigation point, pictures may be added - that reflect our profession and/or the subsection)
What we will need at the end of the day is a fully functional site - i.e: a site that is designed and programmed with backend/wordpress, to allow us to make changes anytime we feel like it.
Further questions?! Don't hesitate to contact me! Thanks :)
Target Market(s)
Real Estate Development/Building sector
Industry/Entity Type
Real Estate Development
Number of Pages Required
5+ page
Look and feel

```html
<!DOCTYPE html>
<html lang="en">
<head>
<meta charset="utf-8">
<title>Kalvoria – Property Developer</title>
<link href="https://fonts.googleapis.com/css2?family=Roboto+Condensed:wght@400;700&family=Open+Sans:wght@400;600&family=Raleway:wght@400&display=swap" rel="stylesheet">
<style>
:root{
  --blue:#0b6aa2;
  --navy:#1c4b79;
  --ink:#222;
  --text:#5a5a5a;
  --line:#d8d8d8;
  --white:#fff;
}
*{margin:0;padding:0;box-sizing:border-box}
html,body{width:735px;height:1200px;overflow:hidden;background:var(--white)}
body{position:relative;font-family:'Open Sans',sans-serif;color:var(--text)}
.abs{position:absolute}
.top-rule{left:0;top:0;width:735px;height:2px;background:var(--navy)}
/* header */
.brand{left:48px;top:14px;display:flex;align-items:center;gap:6px}
.brand-mark{width:20px;height:44px;background:var(--ink)}
.brand-name{font-family:'Roboto Condensed',sans-serif;font-size:36px;line-height:36px;color:var(--ink);letter-spacing:1px}
.brand-sub{font-family:'Roboto Condensed',sans-serif;font-size:9px;color:var(--ink);border-top:1px solid var(--ink);margin-top:1px;padding-top:1px}
.mail{left:386px;top:10px;font-family:'Roboto Condensed',sans-serif;font-size:13px;color:var(--blue);display:flex;align-items:center;gap:6px}
.phone{left:538px;top:0;width:150px;height:34px;background:var(--navy);border-radius:0 0 3px 3px;color:var(--white);font-family:'Roboto Condensed',sans-serif;font-size:15px;display:flex;align-items:center;justify-content:center;gap:7px}
.nav{left:298px;top:42px;display:flex;font-family:'Roboto Condensed',sans-serif;font-size:13px;color:var(--ink)}
.nav a{display:block;height:29px;line-height:29px;padding:0 12px;color:inherit;text-decoration:none}
.nav a.active{background:var(--blue);color:var(--white);border-radius:2px;padding:0 14px}
/* hero */
.hero{left:0;top:87px;width:735px;height:326px;background:linear-gradient(180deg,#9fbde3 0%,#c9d9ee 30%,#d7d6d3 55%,#bdbcba 80%,#a9a8a5 100%)}
.hero-arrow{top:208px;width:44px;height:44px;background:var(--white);border-radius:3px;color:var(--navy);font-family:'Roboto Condensed',sans-serif;font-size:26px;display:flex;align-items:center;justify-content:center}
/* welcome */
.welcome-photo{left:48px;top:478px;width:247px;height:152px;background:linear-gradient(180deg,#3f63d6 0%,#7d93d8 35%,#e6e6e6 55%,#c9c4bd 100%)}
.welcome-title{left:333px;top:444px;font-family:'Roboto Condensed',sans-serif;font-size:26px;color:var(--blue)}
.welcome-copy{left:333px;top:482px;width:358px;font-size:9.6px;line-height:15.3px}
.welcome-copy p+p{margin-top:15px}
.btn{left:332px;top:608px;width:108px;height:32px;background:var(--blue);color:var(--white);font-family:'Roboto Condensed',sans-serif;font-size:14px;display:flex;align-items:center;justify-content:center;gap:6px}
/* benefits */
.benefits{left:0;top:679px;width:735px;height:287px;background:linear-gradient(180deg,#f2f2f2 0%,#dcdcdc 50%,#c4c4c4 100%)}
.benefits-title{left:0;top:712px;width:735px;text-align:center;font-family:'Roboto Condensed',sans-serif;font-size:25px;color:var(--blue)}
.benefits-sub{left:0;top:745px;width:735px;text-align:center;font-family:'Roboto Condensed',sans-serif;font-size:12.5px;color:#444}
.card{top:771px;width:191px;height:159px;background:var(--white);border:1px solid var(--line);border-radius:3px;text-align:center}
.card svg{margin-top:17px}
.card h3{font-family:'Raleway',sans-serif;font-weight:400;font-size:16px;color:var(--blue);margin-top:6px}
.card p{font-size:9.4px;line-height:15.3px;margin:8px 10px 0}
/* partners */
.venture{left:48px;top:996px;width:640px;display:flex;align-items:center;gap:10px;font-family:'Raleway',sans-serif;font-size:23px;color:var(--blue)}
.venture::before,.venture::after{content:"";flex:1;height:1px;background:var(--blue)}
.partner{top:1040px;width:191px;height:82px;border:1px solid var(--line);border-radius:3px;display:flex;align-items:center;justify-content:center;gap:8px;font-family:'Open Sans',sans-serif;font-size:15px;font-weight:600;color:#333}
.partner .dot{width:14px;height:14px;background:var(--blue)}
/* footer */
.footer{left:0;top:1155px;width:735px;height:45px;background:var(--navy);color:var(--white);font-family:'Roboto Condensed',sans-serif;font-size:11.5px}
.footer .copy{position:absolute;left:48px;top:15px}
.footer .copy span{color:var(--ink)}
.social{position:absolute;right:48px;top:15px;display:flex;gap:14px;font-size:11px}
</style>
</head>
<body>
<div class="abs top-rule"></div>

<div class="abs brand">
  <div class="brand-mark"></div>
  <div>
    <div class="brand-name">KALVORIA</div>
    <div class="brand-sub">KALVORIA.EXAMPLE</div>
  </div>
</div>

<div class="abs mail">
  <svg width="13" height="10" viewBox="0 0 13 10"><rect x="0" y="0" width="13" height="10" rx="1" fill="#0b6aa2"/><path d="M1 1.5 6.5 5.5 12 1.5" stroke="#fff" stroke-width="1.2" fill="none"/></svg>
  info@kalvoria.example
</div>
<div class="abs phone">
  <svg width="13" height="13" viewBox="0 0 24 24"><path d="M6.6 10.8a15 15 0 0 0 6.6 6.6l2.2-2.2c.3-.3.7-.4 1-.2 1.1.4 2.3.6 3.6.6.6 0 1 .4 1 1V20c0 .6-.4 1-1 1A17 17 0 0 1 3 4c0-.6.4-1 1-1h3.5c.6 0 1 .4 1 1 0 1.3.2 2.5.6 3.6.1.3 0 .7-.2 1z" fill="#fff"/></svg>
  +43 1 555 0142
</div>

<nav class="abs nav">
  <a class="active">ABOUT</a>
  <a>PROJECTS</a>
  <a>INVESTMENT</a>
  <a>CONTACT</a>
  <a>LEGAL NOTICE</a>
</nav>

<div class="abs hero" role="img" aria-label="Photo of a modern two-storey office building with parked cars under a blue sky"></div>
<div class="abs hero-arrow" style="left:22px">«</div>
<div class="abs hero-arrow" style="left:669px">»</div>

<div class="abs welcome-photo" role="img" aria-label="Rendering of a white terraced apartment building with planted balconies"></div>
<h1 class="abs welcome-title">Welcome to Kalvoria</h1>
<div class="abs welcome-copy">
  <p>Kalvoria is a combination of potent companies pursuing a common goal: the realization of modern, sustainable housing projects for highest demands in Vienna. Our building companies' efforts are concentrating on the two core areas of new developments and roof extensions.</p>
  <p>A high level of expertise, excellent quality and many years of experience provide a solid foundation for the realization of dream homes.</p>
</div>
<div class="abs btn">READ MORE
  <svg width="7" height="11" viewBox="0 0 7 11"><path d="M1 1l4.5 4.5L1 10" stroke="#fff" stroke-width="1.6" fill="none"/></svg>
</div>

<div class="abs benefits" role="img" aria-label="Faded grey photo of a city skyline"></div>
<h2 class="abs benefits-title">OUR BENIFIT</h2>
<div class="abs benefits-sub">EVERYTHING UNDER ONE ROOF.</div>

<div class="abs card" style="left:48px">
  <svg width="38" height="38" viewBox="0 0 38 38"><circle cx="19" cy="19" r="17" fill="#0b6aa2"/><circle cx="19" cy="19" r="11" fill="#fff"/><path d="M13.5 19l4 4 7-8" stroke="#0b6aa2" stroke-width="3" fill="none"/></svg>
  <h3>QUALITY</h3>
  <p>Lorem Ipsum is simply dummy text of the printing and typesetting industry. Lorem Ipsum has been.</p>
</div>
<div class="abs card" style="left:273px">
  <svg width="38" height="38" viewBox="0 0 38 38" fill="none" stroke="#0b6aa2" stroke-width="1.8"><path d="M19 9a8 8 0 0 0-4.5 14.6V27h9v-3.4A8 8 0 0 0 19 9z"/><path d="M15.5 30h7M16.5 33h5M19 2v4M6 14h4M28 14h4M9 5l3 3M29 5l-3 3"/></svg>
  <h3>SKILLS</h3>
  <p>Lorem Ipsum is simply dummy text of the printing and typesetting industry. Lorem Ipsum has been.</p>
</div>
<div class="abs card" style="left:497px">
  <svg width="38" height="38" viewBox="0 0 38 38"><circle cx="15" cy="20" r="10" fill="none" stroke="#0b6aa2" stroke-width="5" stroke-dasharray="4 3"/><circle cx="15" cy="20" r="4" fill="#0b6aa2"/><circle cx="29" cy="10" r="5" fill="none" stroke="#0b6aa2" stroke-width="3.5" stroke-dasharray="3 2"/><circle cx="29" cy="29" r="5" fill="none" stroke="#0b6aa2" stroke-width="3.5" stroke-dasharray="3 2"/></svg>
  <h3>EXPERIENCE</h3>
  <p>Lorem Ipsum is simply dummy text of the printing and typesetting industry. Lorem Ipsum has been.</p>
</div>

<div class="abs venture">Kalvoria is a joint venture between:</div>
<div class="abs partner" style="left:48px"><span class="dot"></span>Velmont Property</div>
<div class="abs partner" style="left:273px">Aldren Haus</div>
<div class="abs partner" style="left:497px"><span class="dot"></span>Norvik Real Estate</div>

<footer class="abs footer">
  <div class="copy">© <span>Kalvoria</span> - 2015. All Rights Reserved.</div>
  <div class="social"><span>Friendbook</span><span>Chirper</span><span>Circles</span></div>
</footer>
</body>
</html>
```